Website Design for Landscaping/Concrete Company

I need a website that is informative about what my company does and also offers before and after pictures of completed work. I already have a logo. The website must say "FREE ESTIMATES" somewhere and list a phone number. I would like to stick with the logo colors or similar (black and lime green).
Services Offered by Dornel Contractors:
Landscaping
Mowing
Concrete
Sidewalks
Brush Removal
Land Beautification

Please list the company name in large letters DORNEL CONTRACTORS
and also the contact information in large font.

Right now I am looking for a somewhat coverpage for my website. I don't have a lot of information for people to point and click on yet. Id like to get a coverpage to get my name out and then have a designer come back in a few months and update with more pictures and information.
Updates

If allowed please submit projects after due date. I made a mistake and only posted for one day. Thanks.

Coding

Coded - Design and coding required

```html
<!DOCTYPE html>
<html lang="en">
<head>
<meta charset="utf-8">
<title>Dornel Contractors</title>
<link href="https://fonts.googleapis.com/css2?family=League+Spartan:wght@400;500;600;700&family=Oswald:wght@400&display=swap" rel="stylesheet">
<style>
:root{
  --lime:#a6c01c;
  --lime-dark:#93ab12;
  --black:#111111;
  --ink:#1c1c1c;
  --white:#ffffff;
  --line:#d9d9d9;
}
*{box-sizing:border-box;margin:0;padding:0}
html,body{width:1200px;height:3493px;overflow:hidden}
body{position:relative;font-family:"League Spartan",sans-serif;color:var(--ink);background:var(--white)}
.abs{position:absolute}
.pill{position:absolute;display:flex;align-items:center;justify-content:center;border-radius:20px;font-size:13px;font-weight:600}

/* header */
.site-header{position:absolute;left:0;top:0;width:1200px;height:120px;background:var(--lime)}
.brand{position:absolute;left:88px;top:28px;display:flex;align-items:center;gap:8px;font-size:17px;font-weight:700;color:var(--black);line-height:1.05;width:120px}
.brand-square{width:18px;height:18px;background:var(--black);flex:none}
.call{position:absolute;left:607px;top:28px;font-family:"Oswald",sans-serif;font-size:16px;color:var(--black);display:flex;align-items:center;gap:6px}
.social{position:absolute;width:32px;height:32px;border-radius:50%;border:1.5px solid var(--black)}
.social.on{background:var(--black)}
.estimate-btn{left:935px;top:24px;width:177px;height:30px;background:var(--black);color:var(--white)}
.nav{position:absolute;top:79px;font-size:14px;font-weight:500;color:var(--black)}
.nav.active{color:var(--white)}

/* hero */
.hero-photo{position:absolute;left:0;top:120px;width:1200px;height:660px;background:linear-gradient(180deg,#4d5a48 0%,#5b6476 35%,#4f5a3f 70%,#6f8a3a 100%)}
.hero-title{position:absolute;left:0;width:1200px;top:326px;text-align:center;font-size:60px;font-weight:700;color:var(--white);letter-spacing:.5px}
.hero-sub{position:absolute;left:0;width:1200px;top:393px;text-align:center;font-size:17px;font-weight:500;color:var(--white)}
.hero-btn{left:536px;top:441px;width:128px;height:32px;background:var(--lime);color:var(--black)}

/* welcome */
.welcome{position:absolute;left:0;top:640px;width:1200px;height:575px}
.welcome-band{position:absolute;left:0;top:90px;width:1200px;height:485px;background:linear-gradient(90deg,var(--lime-dark),var(--lime) 55%,#b0c824)}
.eyebrow{position:absolute;left:88px;top:852px;font-size:19px;font-weight:500;color:var(--black)}
.welcome-title{position:absolute;left:88px;top:880px;font-size:38px;font-weight:500;color:var(--black)}
.lead{position:absolute;left:88px;top:944px;font-size:18.5px;font-weight:600;line-height:19px;letter-spacing:.3px;color:var(--black);white-space:nowrap}
.body-copy{position:absolute;left:88px;top:1003px;font-size:14px;line-height:19.5px;color:var(--black);white-space:nowrap}
.outline-btn{left:88px;top:1107px;width:175px;height:32px;border:1.5px solid var(--black);color:var(--black)}
.emblem{position:absolute;left:848px;top:880px;width:264px;display:flex;flex-direction:column;align-items:center;gap:18px}
.emblem-square{width:150px;height:150px;background:var(--black)}
.emblem-name{font-size:26px;font-weight:700;color:var(--black)}

/* services */
.section-title{position:absolute;left:0;width:1200px;text-align:center;font-size:36px;font-weight:500;color:var(--black)}
.service{position:absolute;width:320px;height:247px;border-bottom:2px solid var(--lime)}
.service .photo{width:320px;height:200px}
.service .label{height:47px;display:flex;align-items:center;justify-content:center;font-size:17px;font-weight:500;color:var(--black)}
.service.active .label{background:var(--lime)}

/* projects */
.projects{position:absolute;left:0;top:1970px;width:1200px;height:620px;background:linear-gradient(135deg,#e2e2e2,#f3f3f3 40%,#dedede 70%,#efefef)}
.project-photo{position:absolute;width:376px;height:239px}
.tag{position:absolute;top:2223px;width:80px;height:30px;border-radius:15px;background:var(--black);color:var(--white);font-size:11px;font-weight:700;display:flex;align-items:center;justify-content:center;letter-spacing:.5px}
.green-btn{background:var(--lime);color:var(--black)}

/* estimate */
.field{position:absolute;border:1px solid var(--line);border-radius:16px;font-size:12px;color:#555;padding:10px 16px}
.submit{left:552px;top:2895px;width:96px;height:30px;border:1.5px solid var(--lime);color:var(--lime)}

/* footer */
.footer-band{position:absolute;left:0;top:3060px;width:1200px;height:433px;background:var(--black)}
.f-head{position:absolute;top:3147px;font-size:16px;font-weight:600;color:var(--white)}
.f-text{position:absolute;left:88px;font-size:12px;color:var(--white)}
.f-call{position:absolute;left:88px;top:3192px;font-family:"Oswald",sans-serif;font-size:17px;color:var(--white);display:flex;gap:6px;align-items:center}
.f-link{position:absolute;left:412px;font-size:12px;color:var(--white)}
.f-link.active{color:var(--lime)}
.f-social{position:absolute;top:3371px;width:30px;height:30px;border-radius:50%;border:1.5px solid var(--lime)}
.f-social.on{background:var(--lime)}
.map{position:absolute;left:616px;top:3149px;width:496px;height:240px;background:linear-gradient(135deg,#ececec,#f6f6f4 50%,#e6e8e4)}
.copy{position:absolute;left:88px;top:3430px;font-size:12px;color:var(--white)}
.copy span{color:var(--lime)}
</style>
</head>
<body>

<header class="site-header">
  <div class="brand"><span class="brand-square"></span>DORNEL CONTRACTORS</div>
  <div class="call">Call Us:
    <svg width="14" height="14" viewBox="0 0 24 24" fill="none" stroke="#111" stroke-width="2"><path d="M22 16.9v3a2 2 0 0 1-2.2 2 19.8 19.8 0 0 1-8.6-3.1 19.5 19.5 0 0 1-6-6A19.8 19.8 0 0 1 2.1 4.2 2 2 0 0 1 4.1 2h3a2 2 0 0 1 2 1.7c.1 1 .4 1.9.7 2.8a2 2 0 0 1-.5 2.1L8 9.9a16 16 0 0 0 6 6l1.3-1.3a2 2 0 0 1 2.1-.4c.9.3 1.8.6 2.8.7a2 2 0 0 1 1.7 2z"/></svg>
    +555-014-2290</div>
  <span class="social" style="left:802px;top:23px" aria-label="Social link"></span>
  <span class="social on" style="left:840px;top:23px" aria-label="Social link"></span>
  <span class="social" style="left:879px;top:23px" aria-label="Social link"></span>
  <div class="pill estimate-btn">Get A Free Estimate</div>
  <span class="nav active" style="left:558px">-- Home --</span>
  <span class="nav" style="left:683px">About Us</span>
  <span class="nav" style="left:804px">Services</span>
  <span class="nav" style="left:920px">Projects</span>
  <span class="nav" style="left:1035px">Contact Us</span>
</header>

<div class="hero-photo" role="img" aria-label="Photo of a blue two-storey house with a lawn and stone path"></div>
<h1 class="hero-title">DORNEL CONTRACTORS</h1>
<p class="hero-sub">It is a long established fact that a reader will be distracted</p>
<div class="pill hero-btn">Contact Us</div>
<svg class="abs" style="left:590px;top:633px" width="20" height="18" viewBox="0 0 20 18" fill="none" stroke="#fff" stroke-width="1.5"><path d="M3 2l7 6 7-6M3 9l7 6 7-6"/></svg>

<section class="welcome">
  <svg class="abs" style="left:0;top:0" width="1200" height="160" viewBox="0 0 1200 160">
    <path d="M0 90 C120 130 230 140 360 120 C560 85 760 20 960 10 C1080 5 1160 20 1200 30 L1200 160 L0 160Z" fill="var(--lime)"/>
    <path d="M0 90 C120 130 230 140 360 120 C560 85 760 20 960 10 C1080 5 1160 20 1200 30" fill="none" stroke="var(--black)" stroke-width="12"/>
  </svg>
  <div class="welcome-band"></div>
</section>
<p class="eyebrow">WELCOME TO</p>
<h2 class="welcome-title">Dornel Contractors</h2>
<p class="lead">Lorem Ipsum is simply dummy text of the printing and typesetting industry.<br>Lorem Ipsum has been the industry's standard dummy text.</p>
<p class="body-copy">There are many variations of passages of Lorem Ipsum available, but the majority have<br>suffered alteration in some form, by injected humour, or randomised words which don't look<br>even slightly believable. If you are going to use a passage of Lorem Ipsum, you need to be sure<br>there isn't anything All the Lorem Ipsum generators on the Internet.</p>
<div class="pill outline-btn">Get A Free Estimate</div>
<div class="emblem"><span class="emblem-square"></span><span class="emblem-name">DORNEL</span></div>

<h2 class="section-title" style="top:1288px">Services We Provide</h2>
<div class="service" style="left:88px;top:1363px"><div class="photo" role="img" aria-label="Worker laying sod rolls" style="background:linear-gradient(135deg,#c9b9a8,#6f8f3a 60%,#3f6a2a)"></div><div class="label">Landscaping</div></div>
<div class="service" style="left:440px;top:1363px"><div class="photo" role="img" aria-label="Lawn mower on green grass" style="background:linear-gradient(180deg,#4f8a2a,#6aa83a)"></div><div class="label">Mowing</div></div>
<div class="service" style="left:792px;top:1363px"><div class="photo" role="img" aria-label="Workers finishing fresh concrete" style="background:linear-gradient(135deg,#a08a70,#9aa7ad 50%,#7f8b90)"></div><div class="label">Concrete</div></div>
<div class="service" style="left:88px;top:1643px"><div class="photo" role="img" aria-label="Curving sidewalk through lawn" style="background:linear-gradient(135deg,#8fa3b5,#c9c9c2 40%,#4e8a2c)"></div><div class="label">Sidewalks</div></div>
<div class="service active" style="left:440px;top:1643px"><div class="photo" role="img" aria-label="Gloved hand scrubbing siding with brush" style="background:linear-gradient(135deg,#f2efe6,#ddd3bd 60%,#e8c24a)"></div><div class="label">Brush Removal</div></div>
<div class="service" style="left:792px;top:1643px"><div class="photo" role="img" aria-label="Park promenade beside a pond" style="background:linear-gradient(180deg,#9ec3e0,#5f8f3a 45%,#b48670 80%,#7d9a8a)"></div><div class="label">Land Beautification</div></div>

<section class="projects"></section>
<h2 class="section-title" style="top:2044px">Our Completed Projects</h2>
<svg class="abs" style="left:88px;top:2260px" width="14" height="26" viewBox="0 0 14 26" fill="none" stroke="#888" stroke-width="1.5"><path d="M12 1L2 13l10 12"/></svg>
<svg class="abs" style="left:1098px;top:2260px" width="14" height="26" viewBox="0 0 14 26" fill="none" stroke="#111" stroke-width="1.5"><path d="M2 1l10 12-10 12"/></svg>
<div class="project-photo" style="left:208px;top:2119px;background:linear-gradient(160deg,#8a8a80,#a6aaa8 40%,#b8946a)" role="img" aria-label="Before: sidewalk being poured"></div>
<div class="project-photo" style="left:616px;top:2119px;background:linear-gradient(180deg,#9ab0b8,#cfcbbf 45%,#b9b2a2)" role="img" aria-label="After: finished concrete sidewalk"></div>
<div class="tag" style="left:505px">BEFORE</div>
<div class="tag" style="left:616px">AFTER</div>
<div class="pill green-btn" style="left:536px;top:2398px;width:128px;height:32px">Contact Us</div>
<svg class="abs" style="left:0;top:2490px" width="1200" height="110" viewBox="0 0 1200 110">
  <path d="M0 40 C120 80 260 95 420 70 C620 40 780 15 960 15 C1080 15 1160 25 1200 35 L1200 110 L0 110Z" fill="var(--white)"/>
  <path d="M0 40 C120 80 260 95 420 70 C620 40 780 15 960 15 C1080 15 1160 25 1200 35" fill="none" stroke="var(--lime)" stroke-width="12"/>
</svg>

<h2 class="section-title" style="top:2642px">Get A Free Estimate</h2>
<div class="field" style="left:208px;top:2719px;width:247px;height:31px">Your Name</div>
<div class="field" style="left:476px;top:2719px;width:247px;height:31px">Email</div>
<div class="field" style="left:744px;top:2719px;width:248px;height:31px">Phone</div>
<div class="field" style="left:208px;top:2772px;width:784px;height:104px">Message ...</div>
<div class="pill submit">Submit</div>

<svg class="abs" style="left:0;top:2980px" width="1200" height="90" viewBox="0 0 1200 90">
  <path d="M0 55 C150 70 300 45 520 38 C760 30 950 8 1200 45 L1200 90 L0 90Z" fill="var(--black)"/>
  <path d="M520 38 C760 30 950 8 1200 45" fill="none" stroke="var(--lime)" stroke-width="10"/>
</svg>
<div class="footer-band"></div>
<h3 class="f-head" style="left:88px">Contact Us</h3>
<div class="f-call">Call Us:
  <svg width="14" height="14" viewBox="0 0 24 24" fill="none" stroke="#fff" stroke-width="2"><path d="M22 16.9v3a2 2 0 0 1-2.2 2 19.8 19.8 0 0 1-8.6-3.1 19.5 19.5 0 0 1-6-6A19.8 19.8 0 0 1 2.1 4.2 2 2 0 0 1 4.1 2h3a2 2 0 0 1 2 1.7c.1 1 .4 1.9.7 2.8a2 2 0 0 1-.5 2.1L8 9.9a16 16 0 0 0 6 6l1.3-1.3a2 2 0 0 1 2.1-.4c.9.3 1.8.6 2.8.7a2 2 0 0 1 1.7 2z"/></svg>
  +555-014-2290</div>
<p class="f-text" style="top:3219px">info@dornel-contractors.com</p>
<p class="f-text" style="top:3262px;line-height:20px">4410 Ashgrove Lane Fenwick,<br>QR 50214</p>
<div class="pill green-btn" style="left:88px;top:3370px;width:175px;height:32px">Get A Free Esstimate</div>
<h3 class="f-head" style="left:412px">Quick Links</h3>
<span class="f-link active" style="top:3192px">Home</span>
<span class="f-link" style="top:3219px">About Us</span>
<span class="f-link" style="top:3246px">Services</span>
<span class="f-link" style="top:3273px">Projects</span>
<span class="f-link" style="top:3300px">Contact Us</span>
<span class="f-social" style="left:413px" aria-label="Social link"></span>
<span class="f-social on" style="left:451px" aria-label="Social link"></span>
<span class="f-social" style="left:490px" aria-label="Social link"></span>
<div class="map" role="img" aria-label="Street map showing the office location"></div>
<p class="copy">© 2020 <span>Dornel Contractors</span>. All Rights Reseved</p>
<svg class="abs" style="left:1102px;top:3420px" width="18" height="20" viewBox="0 0 18 20" fill="none" stroke="var(--lime)" stroke-width="1.8"><path d="M2 19L9 2l7 17M5 13h8"/></svg>

</body>
</html>
```